Useable Postcard Gift for Artistic Convention Use

Useable Postcard Gift Conference Use, search for web designers
Name of the Company is: Verdelume Collective
I have an image that I would like to use for the front of the card
along with a by line which says "Let Each Step Bring Calm to Your Day"
Regarding image, i am good to leave the black behind.... should the designer choose. I also have a black and white image to use as well if someone needs it.

Design Target Market: State of the Art, Hip, Elegant, Conscious

This card will be used at a state of the art tech Brindle Summit in Los Angeles. We want to hand it out to those we are interested in continuing relationship with for the purpose of building a website that is comprehensive. We are looking for designers and tech builders for the site.

This is a service business. I would like to have 3 names and titles on the back of the card and a small paragraph of copy. I like the beauty of the postcard i have saved on my account. I like Copper Gothic, thin lettering and Amazone or Caligraphy where it fits.... if it fits.

I want the card to communicate interest in Verdelume Collective as a state of the art web community that services those progressive professionals who are interested in personal balance and who want to purchase products that are essential to a healthful life.
Updates

Project Deadline Extended
Reason: The deadline is extended through tomorrow due to the need to complete a design. Please continue support

Target Market(s)

High profile clients for coaching, web designers and web technicians for elaborate website build.

Industry/Entity Type

Progressive

Font styles to use
Serif
Script

Colors
00a88f
0555a3
6b449b
ffc214
9bcb3b
f37022

Requirements
Nice to have
• This was supposed to be the must have feature but it wouldn't return there so-----
We want the card to be elegant and definitely a useable postcard.

```html
<!DOCTYPE html>
<html lang="en">
<head>
<meta charset="utf-8">
<title>Verdelume Collective – Postcard Back</title>
<link rel="stylesheet" href="https://fonts.googleapis.com/css2?family=Cinzel:wght@400&family=Alex+Brush&display=swap">
<style>
  :root {
    --ink: #111111;
    --paper: #ffffff;
    --header-orange: #ff8a00;
    --panel-light: #fbfbfb;
    --panel-dark: #d2d2d2;
    --tag-green: #66ff00;
    --tag-shadow: #2f9a12;
    --rule-grey: #8a8a8a;
    --postage-grey: #8f8f8f;
  }
  * { margin: 0; padding: 0; box-sizing: border-box; }
  html, body { width: 1200px; height: 924px; overflow: hidden; background: var(--paper); }
  .postcard {
    position: relative;
    width: 1200px;
    height: 924px;
    background: var(--paper);
    border: 2px solid var(--ink);
    overflow: hidden;
  }
  .info-panel-shape { position: absolute; left: 0; top: 0; }
  .brand-header {
    position: absolute;
    left: 0; top: 0;
    width: 568px; height: 71px;
    background: var(--header-orange);
    border-bottom: 4px solid var(--ink);
    display: flex; align-items: center; justify-content: center;
  }
  .brand-name {
    font-family: "Cinzel", serif;
    font-weight: 400;
    font-size: 37px;
    color: var(--paper);
    letter-spacing: 1px;
  }
  .divider-bar {
    position: absolute;
    left: 570px; top: 0;
    width: 7px; height: 738px;
    background: var(--ink);
  }
  .intro-copy {
    position: absolute;
    left: 24px; top: 84px;
    width: 522px;
    font-family: "Alex Brush", cursive;
    font-size: 27px;
    line-height: 38.2px;
    color: var(--ink);
    text-align: justify;
  }
  .intro-copy p { text-indent: 44px; }
  .team-member { position: absolute; text-align: center; }
  .name-tag {
    position: relative;
    height: 35px;
    background: var(--tag-green);
    font-family: "Cinzel", serif;
    font-size: 23px;
    line-height: 36px;
    color: var(--ink);
    text-align: center;
    box-shadow: -4px 4px 0 -1px var(--tag-shadow);
  }
  .role {
    font-family: "Cinzel", serif;
    font-size: 19px;
    line-height: 25px;
    color: var(--ink);
  }
  .member-one { left: 28px; top: 438px; }
  .member-one .name-tag { width: 374px; margin-left: 3px; }
  .member-one .role { width: 380px; margin-top: 4px; }
  .member-two { left: 102px; top: 551px; }
  .member-two .name-tag { width: 374px; margin-left: 3px; }
  .member-two .role { width: 380px; margin-top: 4px; }
  .member-three { left: 176px; top: 663px; }
  .member-three .name-tag { width: 374px; margin-left: 3px; }
  .member-three .role { width: 380px; margin-top: 4px; }
  .postage-area {
    position: absolute;
    left: 974px; top: 76px;
    width: 138px; height: 139px;
    border: 2px solid var(--postage-grey);
    display: flex; align-items: center; justify-content: center;
    font-family: Arial, Helvetica, sans-serif;
    font-size: 22px; line-height: 28px;
    color: var(--postage-grey);
    text-align: center;
  }
  .address-line {
    position: absolute;
    left: 694px;
    width: 405px;
    height: 2px;
    background: var(--rule-grey);
  }
</style>
</head>
<body>
  <div class="postcard">
    <svg class="info-panel-shape" width="570" height="782" viewBox="0 0 570 782" aria-hidden="true">
      <defs>
        <linearGradient id="panelFade" x1="0" y1="0" x2="0" y2="1">
          <stop offset="0" stop-color="var(--panel-light)"/>
          <stop offset="1" stop-color="var(--panel-dark)"/>
        </linearGradient>
      </defs>
      <path d="M0 72 H570 V738 H190 C160 738 150 778 110 778 H0 Z" fill="url(#panelFade)"/>
    </svg>

    <header class="brand-header">
      <h1 class="brand-name">Verdelume Collective</h1>
    </header>
    <div class="divider-bar"></div>

    <div class="intro-copy">
      <p>We are looking for state of the art web development, design and technical support.</p>
      <p>We are creating a state of the art website that enables personal development tracking, creativity, education, coaching, classes, skill building, privacy for journal and life records and a personal library. The website will have capabilities linking to other sites and services as well.</p>
    </div>

    <div class="team-member member-one">
      <div class="name-tag">Solenne Marwood</div>
      <div class="role">Executive Director<br>Mentor/Coach for Creatives</div>
    </div>
    <div class="team-member member-two">
      <div class="name-tag">Dario Vestrelli</div>
      <div class="role">Operations Director<br>Coach Trainer</div>
    </div>
    <div class="team-member member-three">
      <div class="name-tag">Kenji Aldover</div>
      <div class="role">Operations Assistant</div>
    </div>

    <div class="postage-area">Postage<br>Area</div>
    <div class="address-line" style="top:440px"></div>
    <div class="address-line" style="top:511px"></div>
    <div class="address-line" style="top:581px"></div>
    <div class="address-line" style="top:652px"></div>
  </div>
</body>
</html>
```